MAXI Fest am Lindenbühl - big party night in Straubing

For a party in the Konrad-Weidinger Halle in Straubing, an attractive poster for "party people" is to be created. The poster should attract at least 3000 visitors. The poster (DIN A 2) will be rebuilt by us for further use as an A5 Flyer and should thus ensure the recognition. There are no special conditions regarding colors and design - but the texts mentioned in the annex must be included. The attached photos can be used in any number and / or in excerpts (we will then insert the original high-resolution files ourselves) Important is the communication: Party Where When A reference to the KVMB as organizer is not welcome (except in the imprint) , Although the party takes place in the context of the KVMB Tri-town tour, the poster should primarily address the general party people. The fans around the rally are coming anyway. Pixel Forge - Description Date: 7th May 2018 Title: MAXI Fest am Lindenbühl am 20. October 2018 possible title signature (optional, also changeable) Halle der Helden! or The hall shakes! or hall tremors with 3,000 party people or hall opening at 7 pm - open end Konrad-Weidinger Halle in Straubing Content (all 5 lines compulsory) • Cult band Gustl and the chrome bumpers • Prairie Town with DJ Rodeo shooting booths • Salon Fortuna with roulette Table • Cult figure Kurvnrutscher • Large season-closing party for the KVMB Dreiländer-Tour Website www.dreilaender-tour-ost.de Imprint: Organizer: KVMB Oberpfalz eV, Kestnerweg 12, 80917 Munich E-Mail: motor@opf.kvmb-verein.de, Tel. : 089 - 7462 308 --------------------------------------------- ------------------------------------------ Colors: Free Format: DIN A2 logos : no font: if it is not a design element we prefer Calibri - but remains free to the designer Additional semicolons to the event (for information only): Saturday: The mega-rally party in the Weidinger-Halle From 18 o'clock hall opening - Our Acts : - Gustl and the chrome bumpers (from 20: 30/21 clock) - Prairie Town in Foyer 2 (award ceremony KVMB eV); then open to all with Rodeo etc. (Markus is checking cooperation with Dakota Ranch) and own DJ - show involvement of Verena as a "good mood" host, especially in the time between 6pm and 9pm: Interviews, Acts or Trials the Western-Arena or the casino etc. - The "small" Auwiesenmarkt with dice, Hau the Luke etc.

Colors

Designer to choose colors to be used in the design.

Requirements

```html
<!DOCTYPE html>
<html lang="de">
<head>
<meta charset="utf-8">
<title>MAXI Fest am Lindenbühl – Plakat</title>
<link href="https://fonts.googleapis.com/css2?family=Barlow+Condensed:ital,wght@1,600;1,700;1,800&display=swap" rel="stylesheet">
<style>
  :root {
    --ink: #000000;
    --paper: #ffffff;
    --pink: #e8246d;
    --cyan: #3fbfcf;
    --sky: #06a3dc;
    --yellow: #fbe073;
    --orange: #f0875a;
    --plum: #6a2146;
    --navy: #15213f;
    --coral: #e8667a;
  }
  html, body { margin: 0; padding: 0; overflow: hidden; }
  body { width: 854px; height: 1200px; background: var(--paper); }
  .poster {
    position: relative;
    width: 854px;
    height: 1200px;
    overflow: hidden;
    background: var(--paper);
    font-family: "Barlow Condensed", "Arial Narrow", sans-serif;
    font-style: italic;
    color: var(--paper);
    text-transform: uppercase;
  }
  .poster svg { position: absolute; left: 0; top: 0; }
  .txt { position: absolute; margin: 0; white-space: nowrap; line-height: 1; }

  .title-maxi { left: 70px; top: 58px; font-size: 140px; font-weight: 800; letter-spacing: 2px; }
  .title-fest { left: 62px; top: 172px; font-size: 196px; font-weight: 800; letter-spacing: 3px; }
  .title-place { left: 68px; top: 372px; font-size: 86px; font-weight: 800; letter-spacing: 1px; }

  .date-day { left: 638px; top: 78px; font-size: 74px; font-weight: 800; letter-spacing: 1px; }
  .date-month { left: 640px; top: 144px; font-size: 40px; font-weight: 800; letter-spacing: 1px; }

  .slogan { left: 62px; top: 560px; font-size: 50px; font-weight: 800; }
  .slogan-sub { left: 62px; font-size: 24px; font-weight: 700; letter-spacing: .5px; }
  .slogan-sub.one { top: 620px; }
  .slogan-sub.two { top: 650px; }

  .program { position: absolute; left: 62px; top: 808px; margin: 0; padding: 0; list-style: none;
             font-size: 19px; font-weight: 600; letter-spacing: .5px; line-height: 26.5px; }
  .program li::before { content: "•"; margin-right: 6px; }

  .website { left: 64px; top: 972px; font-size: 32px; font-weight: 800; text-transform: uppercase; }
  .imprint { position: absolute; left: 70px; top: 1010px; margin: 0; font-size: 18px; font-weight: 600;
             line-height: 26.5px; letter-spacing: .4px; }
  .imprint span { display: block; }
</style>
</head>
<body>
<main class="poster">

  <svg class="paint-art" width="854" height="1200" viewBox="0 0 854 1200" role="img"
       aria-label="Bunte Farbspritzer-Illustration in Pink, Türkis, Gelb, Orange und Pflaume als Plakathintergrund">
    <defs>
      <linearGradient id="splash" x1="0" y1="0" x2="1" y2="1">
        <stop offset="0" stop-color="#f6b3a0"/>
        <stop offset=".35" stop-color="#9bdbe2"/>
        <stop offset=".6" stop-color="#f3a6c3"/>
        <stop offset=".85" stop-color="#fbe59a"/>
        <stop offset="1" stop-color="#8fd3de"/>
      </linearGradient>
      <linearGradient id="crowd" x1="0" y1="0" x2="0" y2="1">
        <stop offset="0" stop-color="var(--navy)"/>
        <stop offset=".75" stop-color="#2a2f52"/>
        <stop offset="1" stop-color="#4a8aa8"/>
      </linearGradient>
    </defs>
    <rect width="854" height="1200" fill="url(#splash)"/>
    <path d="M470 0 H854 V400 C800 380 760 330 700 300 C640 270 600 200 560 120 C530 70 500 30 470 0 Z" fill="var(--pink)"/>
    <path d="M0 540 H500 C520 600 520 680 500 730 H0 Z" fill="var(--sky)"/>
    <path d="M520 770 C600 790 700 850 760 930 C820 1000 854 1040 854 1060 V1200 H480 C500 1100 520 980 520 770 Z" fill="url(#crowd)"/>
  </svg>

  <svg class="panels" width="854" height="1200" viewBox="0 0 854 1200" aria-hidden="true">
    <g fill="var(--ink)" stroke="var(--paper)" stroke-width="8" stroke-linejoin="round">
      <path class="title-panel" d="M42 62 Q40 50 55 48 L318 44 Q332 44 332 58 L334 178 L536 176 Q552 176 552 190 L556 352 L630 356 Q644 357 644 372 L646 482 Q646 496 632 496 L50 500 Q36 500 36 486 L34 360 L34 196 Z"/>
      <rect class="date-panel" x="618" y="66" width="198" height="132" rx="28"/>
      <path class="slogan-panel" d="M46 552 Q44 540 58 540 L432 536 Q448 536 450 550 L456 676 Q458 692 442 692 L56 700 Q42 700 42 686 Z"/>
      <path class="info-panel" d="M-20 742 L510 740 Q530 740 540 760 L556 790 Q566 810 548 830 L536 860 Q530 880 552 900 L578 930 Q590 950 570 970 L560 1010 Q556 1030 576 1050 L600 1080 Q610 1100 600 1120 L590 1220 L-20 1220 Z"/>
    </g>
  </svg>

  <h1 class="title">
    <span class="txt title-maxi">MAXI</span>
    <span class="txt title-fest">FEST</span>
    <span class="txt title-place">AM LINDENBÜHL</span>
  </h1>

  <p class="date">
    <span class="txt date-day">AM 20</span>
    <span class="txt date-month">OKT/&nbsp; 2018</span>
  </p>

  <section class="venue">
    <h2 class="txt slogan">HALLE DER HELDEN!</h2>
    <p class="txt slogan-sub one">HALLENBEBEN MIT 3000 PARTY-PEOPLE</p>
    <p class="txt slogan-sub two">KONRAD-WEIDINGER HALLE IN STRAUBING</p>
  </section>

  <ul class="program">
    <li>KULT-BAND GUSTL UND DIE CHROMSTOSSSTANGEN</li>
    <li>PRAIRIE-TOWN MIT DJ + RODEO + WURFBUDEN</li>
    <li>SALON FORTUNA MIT ROULETTE-TISCH</li>
    <li>KULT-FIGUR KURVNRUTSCHER</li>
    <li>GROSSE SAISON-ABSCHLUSSPARTY ZUR KVMB DREILÄNDER-TOUR</li>
  </ul>

  <p class="txt website">WWW.DREILAENDER-TOUR-OST.DE</p>
  <p class="imprint">
    <span>VERANSTALTER: KVMB OBERPFALZ E.V.,</span>
    <span>KESTNERWEG 12, 80917 MÜNCHEN</span>
    <span>E-MAIL: MOTOR@OPF.KVMB-VEREIN.DE,</span>
    <span>TEL.: 089 – 7462 308</span>
  </p>

</main>
</body>
</html>
```